Belford & Company

We are a boutique commercial real estate firm. For our Business card design - sleek, modern, yet high-end/classy. Please see our website: belfordandcompany.example for details.

We currently need 2 business card names and the ability to add/change the business card information -
Name, Title, Address, Office #, Mobile #, Fax, Email and company website.

Industry/Entity Type

Real Estate

Contact Information for Business Card

Business card design - sleek, modern, yet high-end/classy. Please see our website: belfordandcompany.example for details.

Also, we'd like to have our slogan "Precision Guides Every Decision." somewhere in there. We'd like to make some part of it raised or a different texture if possible.
Color #'s:
blue 19 36 128
light gray 222 222 221
dark gray 107 120 128

Also, we'd like to have our slogan "Precision Guides Every Decision." somewhere in there. We'd like to make some part of it raised or a different texture if possible - grey on one side and blue on the other - rounded edges preferred. Maybe either metal/silver/grey raised logo on the back. Thank you!!

Requirements
Must have
• Sleek, modern, clean and classy design

```html
<!DOCTYPE html>
<html lang="en">
<head>
<meta charset="utf-8">
<title>Belford &amp; Company – Business Card</title>
<link href="https://fonts.googleapis.com/css2?family=Open+Sans:wght@400;600;700&display=swap" rel="stylesheet">
<style>
  :root {
    --brand-blue: #1a3594;
    --brand-blue-deep: #142a7e;
    --light-gray: #e6e6e5;
    --paper: #f4f4f3;
    --dark-gray: #6b7880;
    --text-gray: #5f6a70;
    --white: #ffffff;
    --backdrop: #d9dadb;
  }
  * { box-sizing: border-box; margin: 0; padding: 0; }
  html, body { width: 1200px; height: 1021px; overflow: hidden; }
  body {
    background: var(--backdrop);
    font-family: "Open Sans", Arial, sans-serif;
    position: relative;
  }
  .card {
    position: absolute;
    left: 300px;
    width: 600px;
    height: 343px;
    border-radius: 28px;
    overflow: hidden;
    box-shadow: 0 6px 18px rgba(0,0,0,0.18);
  }
  /* Back side */
  .card--back {
    top: 110px;
    background: var(--brand-blue);
    display: flex;
    align-items: center;
    justify-content: center;
  }
  .back-wordmark {
    color: var(--brand-blue-deep);
    font-weight: 700;
    font-size: 40px;
    letter-spacing: 1px;
    white-space: nowrap;
  }
  /* Front side */
  .card--front {
    top: 568px;
    display: flex;
  }
  .front-brand {
    width: 46%;
    background: linear-gradient(135deg, var(--paper), var(--light-gray));
    display: flex;
    flex-direction: column;
    align-items: center;
    justify-content: center;
    padding: 0 16px;
  }
  .brand-plate {
    width: 238px;
    height: 132px;
    background: var(--brand-blue);
    border: 3px solid var(--light-gray);
    outline: 2px solid var(--dark-gray);
    display: flex;
    align-items: center;
    justify-content: center;
    gap: 12px;
    padding: 0 14px;
  }
  .brand-square {
    width: 18px; height: 18px;
    background: var(--light-gray);
    flex: none;
  }
  .brand-name {
    color: var(--white);
    font-weight: 700;
    font-size: 22px;
    line-height: 1.15;
    white-space: nowrap;
  }
  .slogan {
    margin-top: 10px;
    color: var(--text-gray);
    font-size: 15px;
    white-space: nowrap;
  }
  .front-details {
    width: 54%;
    background: var(--dark-gray);
    color: var(--white);
    padding: 34px 16px 0 30px;
  }
  .person-name { font-weight: 700; font-size: 22px; line-height: 1.2; white-space: nowrap; }
  .person-title { font-size: 16px; margin-bottom: 22px; }
  .address { font-size: 15px; line-height: 1.35; margin-bottom: 6px; white-space: nowrap; }
  .contact-list { list-style: none; font-size: 14px; line-height: 1.5; }
  .contact-list li { display: flex; align-items: center; gap: 8px; white-space: nowrap; }
  .contact-list svg { width: 15px; height: 15px; flex: none; fill: none; stroke: var(--white); stroke-width: 1.6; }
</style>
</head>
<body>
  <section class="card card--back" aria-label="Card back">
    <span class="back-wordmark">Belford &amp; Company</span>
  </section>

  <section class="card card--front" aria-label="Card front">
    <div class="front-brand">
      <div class="brand-plate">
        <span class="brand-square"></span>
        <span class="brand-name">Belford &amp;<br>Company</span>
      </div>
      <p class="slogan">Precision Guides Every Decision.</p>
    </div>
    <div class="front-details">
      <p class="person-name">Daniel Hartley</p>
      <p class="person-title">Founder</p>
      <p class="address">2280 Harbor Blvd. Suite #310<br>Riverton, FL 32999</p>
      <ul class="contact-list">
        <li><svg viewBox="0 0 16 16"><path d="M4 2l2.5 3-1.5 1.5a8 8 0 0 0 4.5 4.5L11 9.5l3 2.5-1.5 2A10 10 0 0 1 2 3.5z"/></svg>555.014.2270</li>
        <li><svg viewBox="0 0 16 16"><rect x="4.5" y="1.5" width="7" height="13" rx="1.2"/><line x1="7" y1="12" x2="9" y2="12"/></svg>555.014.2271</li>
        <li><svg viewBox="0 0 16 16"><rect x="4.5" y="1.5" width="7" height="4"/><rect x="1.5" y="5.5" width="13" height="6" rx="1"/><rect x="4.5" y="9.5" width="7" height="5"/></svg>555.014.2272</li>
        <li><svg viewBox="0 0 16 16"><rect x="1.5" y="3.5" width="13" height="9"/><path d="M1.5 3.5l6.5 5 6.5-5"/></svg>daniel@belfordandcompany.example</li>
        <li><svg viewBox="0 0 16 16"><circle cx="8" cy="8" r="6.5"/><ellipse cx="8" cy="8" rx="2.8" ry="6.5"/><line x1="1.5" y1="8" x2="14.5" y2="8"/></svg>www.belfordandcompany.example</li>
      </ul>
    </div>
  </section>
</body>
</html>
```